Vorel!

We need a packaging design for a new company based in Australia called "Vorel".We require a packaging design for a new line of high quality socks we are selling. The socks come in black or white colours and in 3 different sizes. Small, Medium and Large.

The packaging design must be eye catching, classy and up market. The design must fit within the packaging.The design will be printed on a bag that looks like a zipper bag. (see attachment)The bag see through with matt finish. The package size is: Length 24cm (7.8 inches), height 12cm (3.9 inches). We would like to see designs that use the colours blue, red or purple.

Industry/Entity Type

It Company

Requirements
Must have
• The design must contain our company name "Vorel " some where on the packaging with small font and web address. www.vorel.com.au

```html
<!DOCTYPE html>
<html lang="en">
<head>
<meta charset="utf-8">
<title>Vorel – Sock Packaging</title>
<link href="https://fonts.googleapis.com/css2?family=Antonio:wght@300;400&display=swap" rel="stylesheet">
<style>
  :root {
    --magenta: #b82e92;
    --sky: #a6dff7;
    --aqua: #97d7e8;
    --paper: #ffffff;
    --edge: #c8c8c8;
  }
  * { margin: 0; padding: 0; box-sizing: border-box; }
  html, body {
    width: 1200px;
    height: 1000px;
    overflow: hidden;
    background: var(--paper);
  }
  .canvas {
    position: relative;
    width: 1200px;
    height: 1000px;
    background: var(--paper);
  }
  .package {
    position: absolute;
    left: 91px;
    top: 242px;
    width: 1014px;
    height: 507px;
    border: 1px solid var(--edge);
    background: var(--paper);
  }
  .sock-art {
    position: absolute;
    border-radius: 40px 140px 160px 40px;
  }
  .sock-art--magenta {
    left: 43px;
    top: 15px;
    width: 694px;
    height: 240px;
    background: linear-gradient(90deg, var(--sky) 0%, var(--magenta) 12%, var(--magenta) 70%, var(--sky) 100%);
  }
  .sock-art--blue {
    left: 279px;
    top: 268px;
    width: 692px;
    height: 225px;
    background: linear-gradient(90deg, var(--magenta) 0%, var(--aqua) 12%, var(--aqua) 70%, var(--magenta) 100%);
  }
  .brand-name {
    position: absolute;
    right: 30px;
    top: 20px;
    font-family: "Antonio", "Arial Narrow", sans-serif;
    font-weight: 300;
    font-size: 40px;
    line-height: 1;
    letter-spacing: 1px;
    color: var(--magenta);
    text-transform: uppercase;
  }
  .web-address {
    position: absolute;
    left: 20px;
    bottom: 18px;
    font-family: "Antonio", "Arial Narrow", sans-serif;
    font-weight: 400;
    font-size: 15px;
    line-height: 1;
    color: var(--magenta);
    text-transform: uppercase;
  }
</style>
</head>
<body>
  <div class="canvas">
    <section class="package">
      <div class="sock-art sock-art--magenta" role="img" aria-label="Flat illustration of a magenta sock with light blue cuff, heel and toe"></div>
      <div class="sock-art sock-art--blue" role="img" aria-label="Flat illustration of a light blue sock with magenta cuff, heel and toe"></div>
      <h1 class="brand-name">Vorel</h1>
      <p class="web-address">www.vorel.com.au</p>
    </section>
  </div>
</body>
</html>
```